Dental Business Card

I need Dental oriented business cards.
On the front side -
- on the first line, my name:
Dr Marlo Vintner
- on the second line (just underneath):
Doctor of Dental Medicine
- on the third line, or underneath that or in a corner, I would like the address and phone number:
5182 Ch. Birchfield
Montreal QC H2T 4B9
514-629-5074
- other than that i would maybe like a logo of a tooth, but i want it to be subtle and very basic!
- I would like the card to be preferably black or dark grey-ish with the writing in white
On the other side -
- 2-3 lines with the possibility to write the next appointment the box with the lines should be white, with the rest of the card being black

```html
<!DOCTYPE html>
<html lang="en">
<head>
<meta charset="utf-8">
<title>Vintner Dental – Business Card</title>
<link href="https://fonts.googleapis.com/css2?family=Open+Sans:wght@400;600&display=swap" rel="stylesheet">
<style>
  :root {
    --page: #ececec;
    --card: #070707;
    --card-glow: #262626;
    --ink: #ffffff;
    --ink-soft: #bdbdbd;
    --ink-faint: rgba(255,255,255,0.14);
    --note: #ffffff;
    --rule: #1a1a1a;
  }
  * { box-sizing: border-box; margin: 0; padding: 0; }
  html, body { width: 1200px; height: 800px; overflow: hidden; }
  body {
    background: var(--page);
    font-family: "Open Sans", sans-serif;
    display: flex;
    align-items: center;
    justify-content: center;
    gap: 60px;
  }
  .card {
    position: relative;
    width: 520px;
    height: 297px;
    background: radial-gradient(ellipse at 55% 45%, var(--card-glow) 0%, var(--card) 60%);
    border-radius: 4px;
    box-shadow: 0 6px 18px rgba(0,0,0,0.18);
    overflow: hidden;
    color: var(--ink);
  }

  /* Back: appointment side */
  .appointment-box {
    position: absolute;
    left: 34px; top: 58px;
    width: 300px; height: 190px;
    background: var(--note);
    padding: 34px 26px 0;
  }
  .appointment-line {
    height: 1px;
    background: var(--rule);
    margin-bottom: 38px;
  }
  .back-brand {
    position: absolute;
    right: 36px; top: 44px;
    font-size: 13px;
    font-weight: 600;
    color: var(--ink-faint);
    letter-spacing: 0.5px;
  }

  /* Front: identity side */
  .wave {
    position: absolute;
    left: 0; bottom: 0;
    width: 300px; height: 150px;
    background: radial-gradient(ellipse at 40% 80%, rgba(255,255,255,0.07), transparent 70%);
  }
  .brand {
    position: absolute;
    left: 152px; top: 30px;
    display: flex; align-items: center; gap: 8px;
    font-size: 12px;
    font-weight: 600;
    color: var(--ink-soft);
    letter-spacing: 0.4px;
  }
  .brand-dot {
    width: 10px; height: 10px;
    border: 1.5px solid var(--ink-soft);
    border-radius: 50%;
  }
  .identity {
    position: absolute;
    left: 40px; top: 92px;
  }
  .name {
    font-size: 26px;
    font-weight: 600;
    text-transform: uppercase;
    color: #d8d8d8;
    letter-spacing: 0.3px;
  }
  .title {
    font-size: 16px;
    color: var(--ink-soft);
    margin-top: 2px;
  }
  .divider {
    position: absolute;
    left: 322px; top: 70px;
    width: 1px; height: 120px;
    background: linear-gradient(to bottom, transparent, #9a9a9a, transparent);
  }
  .contact {
    position: absolute;
    left: 342px; top: 114px;
    font-size: 14px;
    line-height: 1.35;
    list-style: none;
  }
  .contact li {
    display: flex;
    gap: 9px;
    margin-bottom: 8px;
  }
  .contact svg { flex: none; margin-top: 2px; }
</style>
</head>
<body>

  <section class="card card-back" aria-label="Appointment side">
    <div class="appointment-box">
      <div class="appointment-line"></div>
      <div class="appointment-line"></div>
      <div class="appointment-line"></div>
      <div class="appointment-line"></div>
    </div>
    <div class="back-brand">Vintner Dental</div>
  </section>

  <section class="card card-front" aria-label="Identity side">
    <div class="wave" role="img" aria-label="Soft dark flowing decoration"></div>
    <div class="brand"><span class="brand-dot"></span>Vintner Dental</div>
    <div class="identity">
      <h1 class="name">Dr. Marlo Vintner</h1>
      <p class="title">Doctor of Dental Medicine</p>
    </div>
    <div class="divider"></div>
    <ul class="contact">
      <li>
        <svg width="14" height="18" viewBox="0 0 14 18" fill="none" stroke="#fff" stroke-width="1.4">
          <path d="M7 17 C3 12 1 9.5 1 6.5 A6 6 0 0 1 13 6.5 C13 9.5 11 12 7 17 Z"/>
          <circle cx="7" cy="6.5" r="2.3"/>
        </svg>
        <span>5182 Ch. Birchfield<br>Montreal QC H2T 4B9</span>
      </li>
      <li>
        <svg width="16" height="16" viewBox="0 0 16 16" fill="none" stroke="#fff" stroke-width="1.4">
          <circle cx="8" cy="8" r="7"/>
          <path d="M5.8 4.8 L6.8 6.6 L6 7.4 C6.6 8.6 7.4 9.4 8.6 10 L9.4 9.2 L11.2 10.2 L10.6 11.4 C8 11.2 4.8 8 4.6 5.4 Z" fill="#fff" stroke="none"/>
        </svg>
        <span>514-629-5074</span>
      </li>
    </ul>
  </section>

</body>
</html>
```